Business Card for By Karel Voss

Looking to have a business card designed for my lifestyle and fitness company. My company offers personal training, online programming and nutrition advice based out of London, United Kingdom.

I'd like to see modern, sleek designs, focusing on black, matte black or matte grey. Design doesn't need to be overly descriptive as this will also be used as a personal business card. I've included my logo.

Please note that my company is no longer called "Fitness by Karel Voss" but instead "By Karel Voss", this is because of my other ventures. Therefore please don't use the "fitness by karel voss" text.

information about my company can be found at www.bykarelvoss.com

Company is also based out of London (United Kingdom) & Sydney (Australia) this could be reflected on the card.

Industry/Entity Type

Business

Contact Information for Business Card

Karel Voss
+44 7382 615027
karel@bykarelvoss.com
www.bykarelvoss.com

Font styles to use
Sans Serif

Requirements
Must have
• All contact details and inclusion of my logo.

```html
<!DOCTYPE html>
<html lang="en">
<head>
<meta charset="utf-8">
<title>Business Card – Karel Voss</title>
<link rel="stylesheet" href="https://fonts.googleapis.com/css2?family=Open+Sans:wght@400;600&display=swap">
<style>
  :root {
    --backdrop: #2e2926;
    --card: #1f1f1f;
    --card-edge: #2a2a2a;
    --ink: #f2f2f2;
    --ink-soft: #d6d6d6;
    --rule: #8a8a8a;
    --icon-glyph: #1f1f1f;
  }
  * { box-sizing: border-box; margin: 0; padding: 0; }
  html, body {
    width: 1200px;
    height: 764px;
    overflow: hidden;
    background: var(--backdrop);
    font-family: "Open Sans", sans-serif;
  }
  .stage {
    position: relative;
    width: 1200px;
    height: 764px;
  }
  .card {
    position: absolute;
    top: 227px;
    width: 540px;
    height: 310px;
    background: var(--card);
    border: 1px solid var(--card-edge);
    border-radius: 3px;
    color: var(--ink);
  }
  .card--front { left: 40px; }
  .card--back { left: 620px; }

  .brand {
    position: absolute;
    display: flex;
    flex-direction: column;
    align-items: center;
    gap: 14px;
  }
  .brand__mark {
    width: 46px;
    height: 46px;
    background: var(--ink);
  }
  .brand__name {
    font-weight: 600;
    color: var(--ink);
    text-align: center;
    line-height: 1.15;
    white-space: nowrap;
  }
  .card--front .brand {
    left: 0;
    top: 0;
    width: 262px;
    height: 310px;
    justify-content: center;
  }
  .card--front .brand__name {
    font-size: 20px;
    letter-spacing: 0.5px;
    text-transform: uppercase;
  }
  .divider {
    position: absolute;
    left: 262px;
    top: 46px;
    width: 1px;
    height: 218px;
    background: var(--rule);
  }
  .contact {
    position: absolute;
    left: 300px;
    top: 70px;
  }
  .contact__name {
    font-size: 16px;
    font-weight: 400;
    margin-bottom: 26px;
  }
  .contact__list { list-style: none; }
  .contact__item {
    display: flex;
    align-items: center;
    gap: 10px;
    font-size: 12.5px;
    color: var(--ink-soft);
    margin-bottom: 8px;
  }
  .contact__icon {
    width: 13px;
    height: 13px;
    flex: none;
  }

  .card--back .brand {
    left: 0;
    top: 0;
    width: 540px;
    height: 310px;
    justify-content: center;
  }
  .card--back .brand__mark { width: 58px; height: 58px; }
  .card--back .brand__name {
    font-size: 22px;
    letter-spacing: 1px;
    text-transform: uppercase;
  }
</style>
</head>
<body>
<main class="stage">
  <section class="card card--front" aria-label="Card front">
    <div class="brand">
      <div class="brand__mark"></div>
      <p class="brand__name">By Karel Voss</p>
    </div>
    <div class="divider"></div>
    <div class="contact">
      <p class="contact__name">Karel Voss</p>
      <ul class="contact__list">
        <li class="contact__item">
          <svg class="contact__icon" viewBox="0 0 13 13" aria-hidden="true">
            <rect width="13" height="13" rx="1.5" fill="var(--ink)"/>
            <rect x="4" y="2" width="5" height="9" rx="1" fill="none" stroke="var(--icon-glyph)" stroke-width="1.1"/>
            <rect x="6" y="9" width="1" height="1" fill="var(--icon-glyph)"/>
          </svg>
          <span>+44 7382 615027</span>
        </li>
        <li class="contact__item">
          <svg class="contact__icon" viewBox="0 0 13 13" aria-hidden="true">
            <rect width="13" height="13" rx="1.5" fill="var(--ink)"/>
            <rect x="2.5" y="3.5" width="8" height="6" fill="none" stroke="var(--icon-glyph)" stroke-width="1"/>
            <path d="M2.5 3.5 L6.5 7 L10.5 3.5" fill="none" stroke="var(--icon-glyph)" stroke-width="1"/>
          </svg>
          <span>karel@bykarelvoss.com</span>
        </li>
        <li class="contact__item">
          <svg class="contact__icon" viewBox="0 0 13 13" aria-hidden="true">
            <rect width="13" height="13" rx="1.5" fill="var(--ink)"/>
            <circle cx="6.5" cy="6.5" r="4" fill="none" stroke="var(--icon-glyph)" stroke-width="1"/>
            <ellipse cx="6.5" cy="6.5" rx="1.7" ry="4" fill="none" stroke="var(--icon-glyph)" stroke-width="0.9"/>
            <line x1="2.5" y1="6.5" x2="10.5" y2="6.5" stroke="var(--icon-glyph)" stroke-width="0.9"/>
          </svg>
          <span>www.bykarelvoss.com</span>
        </li>
      </ul>
    </div>
  </section>

  <section class="card card--back" aria-label="Card back">
    <div class="brand">
      <div class="brand__mark"></div>
      <p class="brand__name">Karel Voss</p>
    </div>
  </section>
</main>
</body>
</html>
```